Progressive Architecture and Urban Planning Studio - Stationery Design

The Kestrel Collective: a small boutique Architectural and Urban Planning Studio based in Natal/ RN, Brazil, about to open branches in South Africa and West Africa, established to provide high quality, innovative design and personal client service for projects worldwide. Our approach to Architecture: Minimal - Less is More, so to speak, but with an edge! Strive to produce "clean" projects - stripped of all that can be stripped, no excesses. Got our Logo right here with Pixel Harbor, and hope to do the same with our stationery (were informed that includes business cards, letterhead and envelopes). Since we'll be using two clour schemes, we want at least one using a black background (business card). We'll also allow manipulation of our logo if it helps the final design. Good Luck!

Font styles to use
Other font styles liked:
• Nexa

Colors

Designer to choose colors to be used in the design.

Requirements
Must have
• Business Cards/ Letterheads with the following address:
Rua Olavo Pereira 2741, Vale Dourado, Natal/RN
Should be able to edit it.

```html
<!DOCTYPE html>
<html lang="en">
<head>
<meta charset="utf-8">
<title>The Kestrel Collective – Stationery</title>
<link rel="stylesheet" href="https://fonts.googleapis.com/css2?family=Montserrat:wght@400;700&family=Quicksand:wght@400;700&family=Open+Sans:wght@400&family=Arimo:wght@700&display=swap">
<style>
  :root {
    --ink: #111111;
    --paper: #ffffff;
    --brand-red: #c8191e;
    --mark-tint: #fbe4e4;
    --logo-bg: #f6f6f6;
    --guide: #8a8a8a;
    --rule: #4a5560;
    --edge-shadow: #9a9aa0;
  }
  * { box-sizing: border-box; margin: 0; padding: 0; }
  html, body { width: 781px; height: 1200px; overflow: hidden; background: var(--paper); }
  .sheet { position: relative; width: 781px; height: 1200px; color: var(--ink); }

  .label { position: absolute; font: 13px "Open Sans", sans-serif; color: var(--ink); }

  .guide { position: absolute; border: 1px dashed var(--guide); }

  .card-front {
    position: absolute; left: 0; top: 0; width: 414px; height: 241px;
    border-right: 3px solid var(--ink); border-bottom: 2px solid var(--edge-shadow);
    background: var(--paper);
  }
  .wordmark {
    display: flex; align-items: center; gap: 14px;
    background: var(--logo-bg);
    font-family: "Montserrat", sans-serif; font-weight: 400; color: var(--ink);
    text-transform: uppercase; white-space: nowrap;
  }
  .wordmark-square { background: var(--brand-red); flex: none; }
  .card-front .wordmark { left: 5px; top: 3px; width: 398px; height: 55px; padding-left: 10px; font-size: 17px; letter-spacing: 3.2px; }
  .card-front .wordmark-square { width: 36px; height: 36px; }

  .holder-name, .holder-title { font-family: "Arimo", sans-serif; font-weight: 700; padding-left: 3px; }
  .holder-name { left: 0; top: 113px; width: 154px; height: 24px; font-size: 12px; line-height: 14px; }
  .holder-title { left: 0; top: 137px; width: 154px; height: 25px; font-size: 10px; line-height: 14px; }

  .check-band { position: absolute; left: 0; top: 188px; width: 409px; height: 47px; display: flex; }
  .check-band span { width: 45.5px; height: 47px; border: 1px dashed var(--guide); }
  .check-band .dark { background: var(--ink); }

  .divider { position: absolute; left: 0; width: 411px; border-top: 1px dotted var(--rule); }

  .faint-mark { display: flex; align-items: center; justify-content: center; }
  .faint-mark span { display: block; background: var(--mark-tint); }
  .card-back-mark { left: 125px; top: 262px; width: 184px; height: 176px; }
  .card-back-mark span { width: 130px; height: 130px; }

  .card-address {
    left: 50px; top: 450px; width: 355px; height: 34px; padding: 2px 5px;
    font: 700 12px/14px "Quicksand", sans-serif;
  }
  .card-address span { display: block; white-space: nowrap; }

  .letterhead {
    position: absolute; left: 5px; top: 507px; width: 487px; height: 633px;
    border: 1px solid var(--ink); box-shadow: 3px 3px 0 var(--edge-shadow); background: var(--paper);
  }
  .letterhead .wordmark { left: 15px; top: 12px; width: 208px; height: 30px; padding-left: 4px; gap: 8px; font-size: 9.5px; letter-spacing: 1.3px; border: 0; }
  .letterhead .wordmark-square { width: 20px; height: 20px; }
  .letterhead-mark { left: 145px; top: 222px; width: 195px; height: 175px; border: 0; }
  .letterhead-mark span { width: 150px; height: 150px; }
  .letterhead-address {
    left: 40px; top: 596px; width: 407px; height: 27px; padding-left: 4px;
    font: 400 12px/25px "Quicksand", sans-serif; white-space: nowrap;
  }
</style>
</head>
<body>
<main class="sheet">

  <section class="card-front" aria-label="Business card, front">
    <div class="guide wordmark"><span class="wordmark-square"></span>The Kestrel Collective</div>
    <div class="guide holder-name">Your Name</div>
    <div class="guide holder-title">Your Title</div>
    <div class="check-band" aria-hidden="true">
      <span class="dark"></span><span></span><span class="dark"></span><span></span><span class="dark"></span><span></span><span class="dark"></span><span></span><span class="dark"></span>
    </div>
  </section>
  <p class="label" style="left:510px;top:41px;">Card Front Side</p>

  <div class="divider" style="top:253px;"></div>

  <section aria-label="Business card, back">
    <div class="guide faint-mark card-back-mark"><span></span></div>
    <div class="guide card-address">
      <span>Postal Address :Rua Olavo Pereira 2741,</span>
      <span>Vale Dourado, Natal/RN</span>
    </div>
  </section>
  <p class="label" style="left:516px;top:287px;">Card Back Side</p>

  <div class="divider" style="top:487px;"></div>

  <section class="letterhead" aria-label="Letterhead">
    <div class="guide wordmark"><span class="wordmark-square"></span>The Kestrel Collective</div>
    <div class="guide faint-mark letterhead-mark"><span></span></div>
    <div class="guide letterhead-address">Postal Addresss :Rua Olavo Pereira 2741, Vale Dourado, Natal/RN</div>
  </section>
  <p class="label" style="left:515px;top:517px;">Letter Head</p>

</main>
</body>
</html>
```